Gutscheine für Massage Salon
Zielgruppe
Es handelt dich um einen Massage Salon mit dem Namen „Lindwerk Oase Massage“ Zielgruppe im Prinzip alle Menschen. Es werden verschiedene Massagearten angeboten, von Traditioneller Chinesischer, Thai bis Gesichtsmassage!. Auf der Webseite ersichtlich.
Aufgabenstellung
Der Gutschein soll hochwertig erscheinen und im Querformat mit Kuvert überreicht werden. Auch das Kuvert sollte bedruckt werden. Inhalte wie Gültigkeit, Gutscheinwert, Platz für Unterschrift, Ausstellungsdatun und Stempel sollen vorhanden sein. Platz für den Namen der den Gutschein als Geschenk erhält! Gutschein beidseitig bedruckt. In Bezug suf die Gültigkeit, bitte ich zu berücksichtigen, das lt. Gesetz der Gutschein 5 Jahre ab Kaufdatum gültig ist.

```html
<!DOCTYPE html>
<html lang="de">
<head>
<meta charset="utf-8">
<title>Lindwerk Oase Massage – Gutschein</title>
<link href="https://fonts.googleapis.com/css2?family=Poppins:wght@500;600;700;800&display=swap" rel="stylesheet">
<style>
  :root {
    --backdrop: #c5ae8e;
    --paper: #f6f6f5;
    --paper-shade: #e9e9e7;
    --orange: #c8782f;
    --gold: #c49a5a;
    --text-grey: #7a7774;
    --white: #ffffff;
  }
  * { box-sizing: border-box; margin: 0; padding: 0; }
  html, body {
    width: 1200px; height: 1117px; overflow: hidden;
    background: var(--backdrop);
    font-family: "Poppins", sans-serif;
  }
  .voucher {
    position: absolute; left: 71px; width: 1057px; height: 426px;
    overflow: hidden;
    background: radial-gradient(ellipse at 55% 45%, var(--paper) 0%, var(--paper-shade) 100%);
    box-shadow: 4px 6px 10px rgba(80, 55, 25, 0.35);
  }
  .voucher--front { top: 114px; }
  .voucher--back { top: 578px; }
  .voucher__shapes { position: absolute; inset: 0; }

  .brand { position: absolute; text-align: center; color: var(--orange); font-weight: 700; line-height: 1; }
  .brand__name { display: block; font-size: 40px; letter-spacing: -0.5px; }
  .brand__kind { display: block; font-size: 21px; letter-spacing: 9px; margin-top: 8px; }
  .voucher--front .brand { left: 328px; top: 66px; width: 400px; }
  .voucher--back .brand { left: 30px; top: 32px; width: 290px; }
  .voucher--back .brand__name { font-size: 33px; }
  .voucher--back .brand__kind { font-size: 18px; letter-spacing: 8px; }

  .services {
    position: absolute; left: 328px; top: 148px; width: 400px;
    text-align: center; font-size: 9.5px; font-weight: 500; color: var(--orange);
    letter-spacing: 0.2px;
  }
  .headline {
    position: absolute; left: 328px; top: 195px; width: 400px;
    text-align: center; font-size: 45px; font-weight: 800; color: var(--gold);
    letter-spacing: 1px; line-height: 1;
  }
  .blurb {
    position: absolute; text-align: center; font-weight: 600; color: var(--text-grey);
  }
  .voucher--front .blurb { left: 380px; top: 284px; width: 285px; font-size: 11px; line-height: 13.6px; }
  .voucher--back .blurb { left: 380px; top: 318px; width: 290px; font-size: 9.2px; line-height: 11.4px; }

  .website {
    position: absolute; left: 363px; width: 400px; text-align: center;
    font-size: 17px; font-weight: 700; color: var(--white); letter-spacing: 0.2px;
  }
  .voucher--front .website { top: 388px; }
  .voucher--back .website { top: 391px; }

  .value {
    position: absolute; left: 682px; top: 176px; width: 232px;
    text-align: center; color: var(--white); font-weight: 800; line-height: 1;
  }
  .value__amount { display: block; font-size: 104px; letter-spacing: -3px; }
  .value__unit { display: block; font-size: 33px; margin-top: -2px; }

  .fields { position: absolute; left: 375px; top: 34px; width: 330px; }
  .field { position: relative; height: 42.4px; }
  .field__label { font-size: 12px; font-weight: 700; color: var(--gold); }
  .field__line {
    position: absolute; left: 79px; right: 0; top: 10px;
    border-bottom: 1px solid var(--gold);
  }
  .field--signature { margin-top: 20px; }
  .field--signature .field__line { right: 124px; }
</style>
</head>
<body>

<section class="voucher voucher--front" aria-label="Gutschein Vorderseite">
  <svg class="voucher__shapes" width="1057" height="426" viewBox="0 0 1057 426">
    <defs>
      <linearGradient id="lobbyTones" x1="0" y1="0" x2="1" y2="1">
        <stop offset="0" stop-color="#efe6da"/>
        <stop offset="0.55" stop-color="#b8aa98"/>
        <stop offset="1" stop-color="#2a2522"/>
      </linearGradient>
      <linearGradient id="receptionTones" x1="0" y1="0" x2="1" y2="1">
        <stop offset="0" stop-color="#f7f4ef"/>
        <stop offset="0.6" stop-color="#d9cfc2"/>
        <stop offset="1" stop-color="#3a3330"/>
      </linearGradient>
      <radialGradient id="blossomTones" cx="0.5" cy="0.55" r="0.5">
        <stop offset="0" stop-color="#e9d2b8"/>
        <stop offset="0.45" stop-color="#faf7f2"/>
        <stop offset="1" stop-color="#ece6de"/>
      </radialGradient>
    </defs>
    <ellipse role="img" aria-label="Foto: Empfangsbereich des Salons mit Regal, Pflanzen und Hängeleuchten" cx="116" cy="369" rx="257" ry="307" fill="url(#lobbyTones)"/>
    <circle role="img" aria-label="Foto: Empfangstheke mit Wandbild und Vorhängen" cx="948" cy="146" r="226" fill="url(#receptionTones)"/>
    <rect x="363" y="378" width="694" height="48" fill="var(--orange)"/>
    <ellipse role="img" aria-label="Illustration: weiße Blüte" cx="975" cy="350" rx="125" ry="135" fill="url(#blossomTones)"/>
    <circle cx="798" cy="292" r="116" fill="var(--gold)"/>
  </svg>

  <div class="brand"><span class="brand__name">Lindwerk Oase</span><span class="brand__kind">Massage</span></div>
  <p class="services">TRADITIONELLER CHINESISCHER | THAI | GESICHTSMASSAGE!</p>
  <h1 class="headline">VERWENDEN</h1>
  <p class="blurb">Lorem ipsum dolor sit amet, consectetur adipiscing elit, sed do eiusmod tempor incididunt ut labore et dolore Ut enim ad minim veniam, quis nostrud exercitation ullamco laboris nisi ut aliquip ex ea commodo consequat.</p>
  <p class="website">www.lindwerk-oase-massage.at</p>
  <div class="value"><span class="value__amount">60</span><span class="value__unit">MINUTEN</span></div>
</section>

<section class="voucher voucher--back" aria-label="Gutschein Rückseite">
  <svg class="voucher__shapes" width="1057" height="426" viewBox="0 0 1057 426">
    <defs>
      <linearGradient id="shelfTones" x1="0" y1="0" x2="1" y2="1">
        <stop offset="0" stop-color="#eef1f2"/>
        <stop offset="0.6" stop-color="#c9c4bc"/>
        <stop offset="1" stop-color="#5a4a3c"/>
      </linearGradient>
      <linearGradient id="roomTones" x1="0" y1="0" x2="1" y2="1">
        <stop offset="0" stop-color="#c98a4a"/>
        <stop offset="0.5" stop-color="#8a5a36"/>
        <stop offset="1" stop-color="#4a3022"/>
      </linearGradient>
      <linearGradient id="streetTones" x1="0" y1="0" x2="0" y2="1">
        <stop offset="0" stop-color="#dcd8cf"/>
        <stop offset="1" stop-color="#8f8a82"/>
      </linearGradient>
      <linearGradient id="bottleTones" x1="0" y1="0" x2="0" y2="1">
        <stop offset="0" stop-color="#a9c2cf"/>
        <stop offset="1" stop-color="#6b5644"/>
      </linearGradient>
      <radialGradient id="blossomTonesBack" cx="0.5" cy="0.55" r="0.5">
        <stop offset="0" stop-color="#e9d2b8"/>
        <stop offset="0.45" stop-color="#faf7f2"/>
        <stop offset="1" stop-color="#ece6de"/>
      </radialGradient>
    </defs>
    <ellipse role="img" aria-label="Foto: Glasregal mit Massageölen und Buddha-Figur" cx="116" cy="420" rx="257" ry="320" fill="url(#shelfTones)"/>
    <circle role="img" aria-label="Foto: Behandlungsraum mit Massageliege" cx="955" cy="147" r="232" fill="url(#roomTones)"/>
    <rect x="369" y="380" width="688" height="46" fill="var(--orange)"/>
    <ellipse role="img" aria-label="Illustration: weiße Blüte" cx="965" cy="350" rx="125" ry="125" fill="url(#blossomTonesBack)"/>
    <circle role="img" aria-label="Foto: Straßenansicht des Salons" cx="886" cy="256" r="75" fill="url(#streetTones)" stroke="#f7efe6" stroke-width="5"/>
    <circle role="img" aria-label="Foto: Fläschchen mit Massageölen" cx="753" cy="334" r="72" fill="url(#bottleTones)" stroke="#f7efe6" stroke-width="5"/>
  </svg>

  <div class="brand"><span class="brand__name">Lindwerk Oase</span><span class="brand__kind">Massage</span></div>

  <div class="fields">
    <div class="field"><span class="field__label">Date</span><span class="field__line"></span></div>
    <div class="field"><span class="field__label">To:</span><span class="field__line"></span></div>
    <div class="field"><span class="field__label">From:</span><span class="field__line"></span></div>
    <div class="field"><span class="field__label">A gift of:</span><span class="field__line"></span></div>
    <div class="field"><span class="field__label">Valid until:</span><span class="field__line"></span></div>
    <div class="field field--signature"><span class="field__label">Signature:</span><span class="field__line"></span></div>
  </div>

  <p class="blurb">Lorem ipsum dolor sit amet, consectetur adipiscing elit, sed do eiusmod tempor incididunt ut labore et dolore Ut enim ad minim veniam, quis nostrud exercitation ullamco laboris nisi ut aliquip ex ea commodo consequat.</p>
  <p class="website">www.lindwerk-oase-massage.at</p>
</section>

</body>
</html>
```